plumbing & gas fitting business card design

We need a business card design for a plumbing & gas fitting company. The company covers commercial, domestic and maintenance work. We would like a modern design communicating efficiency and sophistication. preferred colours would include (red grey & black) or (green grey & black). Please DO NOT include any water droplets.

Varcoe Plumbing & Gas, Commercial Domestic & Maintenance, licence no. 418736K, ABN 57204918362, Phone 0417382965, Email varcoeplumbingandgas@tidemail.com

```html
<!DOCTYPE html>
<html lang="en">
<head>
<meta charset="utf-8">
<title>Varcoe Plumbing &amp; Gas — Stationery</title>
<link href="https://fonts.googleapis.com/css2?family=Cabin:ital,wght@0,400;1,400&family=Spectral:wght@600&display=swap" rel="stylesheet">
<style>
  :root {
    --backdrop: #f3f3f3;
    --paper: #ebebeb;
    --ink: #1c1c1c;
    --ink-soft: #2a2a2a;
    --label-grey: #a9a9a9;
    --accent-green: #7db536;
  }
  * { margin: 0; padding: 0; box-sizing: border-box; }
  html, body { width: 1200px; height: 1000px; overflow: hidden; }
  body {
    position: relative;
    background: var(--backdrop);
    font-family: "Cabin", Arial, sans-serif;
    color: var(--ink);
  }
  .sheet, .card { position: absolute; background: var(--paper); }

  .letterhead { left: 135px; top: 190px; width: 458px; height: 620px; }
  .letterhead .wordmark {
    position: absolute; top: 18px; left: 0; width: 100%;
    text-align: center; font-size: 12px;
  }

  .wordmark {
    font-family: "Spectral", Georgia, serif;
    font-weight: 600;
    color: var(--ink);
    text-transform: uppercase;
    letter-spacing: 0.2px;
    white-space: nowrap;
  }

  .card { left: 645px; width: 421px; height: 241px; }
  .card-front { top: 297px; }
  .card-back { top: 570px; height: 240px; }

  .services {
    position: absolute; top: 15px; left: 12px; right: 12px;
    font-style: italic; font-size: 11px; color: var(--label-grey);
  }
  .services span { position: absolute; top: 0; }
  .services .commercial { left: 0; }
  .services .domestic { left: 160px; }
  .services .maintenance { left: 298px; }

  .card-front .wordmark {
    position: absolute; left: 12px; top: 92px; font-size: 17px;
  }

  .contact { position: absolute; left: 172px; top: 165px; font-size: 13px; color: var(--ink-soft); line-height: 17px; }
  .credentials {
    position: absolute; top: 214px; left: 172px; right: 12px;
    font-style: italic; font-size: 11px; color: var(--ink-soft);
  }
  .credentials span { position: absolute; top: 0; }
  .credentials .licence { left: 0; }
  .credentials .abn { left: 138px; }

  .card-back .wordmark {
    position: absolute; left: 0; right: 0; top: 104px;
    text-align: center; font-size: 22px;
  }
</style>
</head>
<body>
  <section class="sheet letterhead">
    <div class="wordmark">Varcoe Plumbing &amp; Gas</div>
  </section>

  <section class="card card-front">
    <div class="services">
      <span class="commercial">Commercial</span>
      <span class="domestic">Domestic</span>
      <span class="maintenance">Maintenance</span>
    </div>
    <div class="wordmark">Varcoe Plumbing &amp; Gas</div>
    <div class="contact">
      <div class="phone">041-738-2965</div>
      <div class="email">varcoeplumbingandgas@tidemail.com</div>
    </div>
    <div class="credentials">
      <span class="licence">Licence No. 418736K</span>
      <span class="abn">ABN 57204918362</span>
    </div>
  </section>

  <section class="card card-back">
    <div class="wordmark">Varcoe Plumbing &amp; Gas</div>
  </section>
</body>
</html>
```